Willowmere Commons Shopping Center Brochure

Take the three attached files, request any additional information that may be needed and produce an attractive and effective pdf marketing brochure that will help make our shopping center lease up.  Would prefer most, if not all, of the text in the word file to be included.  Other than that parameter we are looking for a winning look.  The attached pdf file has too much information and ONLY page one should be used.  We would like all the tables and accompanying text in the Excel workbook to be used.
Thank you!

Target Market(s)
Entrepreneurs who need a commercial retail space to operate their businesses from.
Industry/Entity Type
Marketing
Look and feel
Each slider illustrates characteristics of the customer's brand and the style your logo design should communicate.

```html
<!DOCTYPE html>
<html lang="en">
<head>
<meta charset="utf-8">
<title>Willowmere Commons Shopping Center Brochure</title>
<link rel="stylesheet" href="https://fonts.googleapis.com/css2?family=Anton&family=Dancing+Script:wght@600&family=Open+Sans:wght@400;700;800&family=PT+Sans:wght@400;700&display=swap">
<style>
:root{
  --olive:#d6c866;--olive-light:#efe6a6;--olive-dark:#a99a3a;
  --aqua:#8fdcec;--aqua-light:#d9f4f9;--sky:#6fcde4;
  --orange:#f28a3a;--orange-light:#f7b57a;--red:#e5413a;
  --green:#7cc242;--green-light:#b8e08a;--blue:#3f9fd6;--blue-light:#7cc6ec;
  --grey:#8f8f86;--ink:#1d1d1d;--white:#fff;--cream:#fffbe6;
}
*{box-sizing:border-box;margin:0;padding:0}
html,body{width:859px;height:1200px;overflow:hidden;background:#fff}
body{font-family:"PT Sans",Arial,sans-serif;color:var(--ink);position:relative}
.canvas{position:relative;width:859px;height:1200px;overflow:hidden}
.panel-labels{position:absolute;left:0;width:859px;height:34px;display:flex}
.panel-labels .lbl{flex:1;text-align:center;font:700 11px/1.25 "Open Sans",Arial,sans-serif;border-right:1px dashed #999}
.panel-labels .lbl:last-child{border-right:none}
.panel{position:absolute;overflow:hidden}
.ph{position:absolute;border-radius:2px}

/* outside left */
.out-left{left:0;top:36px;width:281px;height:556px;background:linear-gradient(180deg,var(--olive-light),var(--olive) 60%,var(--olive-light))}
.sec-title{font:700 13px "Open Sans",Arial,sans-serif;color:#fff;text-align:center;letter-spacing:1px}
.out-left .sec-title{position:absolute;top:8px;width:100%;color:#fff;text-shadow:0 0 2px var(--olive-dark)}
.map{left:8px;top:28px;width:265px;height:180px;background:linear-gradient(135deg,#f3efd5,#e9e3c2)}
.photo-a{left:8px;top:214px;width:265px;height:80px;background:linear-gradient(180deg,#b9d3e8 0%,#cfdfe9 40%,#7f8a6d 62%,#9a9a8f 100%)}
.traffic-title{position:absolute;top:298px;width:100%;text-align:center;font:700 7px "Open Sans",Arial,sans-serif;color:#fff7b0;letter-spacing:.5px}
.traffic-heads{position:absolute;top:307px;left:8px;width:265px;display:grid;grid-template-columns:repeat(4,1fr);justify-items:center}
.traffic-heads span{width:38px;height:38px;border-radius:50%;background:var(--orange-light);border:2px solid #fff;display:flex;align-items:center;justify-content:center;text-align:center;font:700 5.5px/1.1 "Open Sans",Arial,sans-serif;color:#fff}
.traffic{position:absolute;left:4px;top:347px;width:273px;background:#fff;border-collapse:collapse;font:700 7px "PT Sans",Arial,sans-serif}
.traffic td{height:18.6px;border-left:2px solid var(--orange);border-right:2px solid var(--orange);padding:0 3px;white-space:nowrap}
.traffic td:first-child{text-align:right;width:30%}
.traffic td:nth-child(3),.traffic td:nth-child(4){text-align:right}
.tagline{position:absolute;bottom:4px;left:10px;font:600 8px "Dancing Script",cursive;color:#fff}

/* outside central */
.out-central{left:283px;top:36px;width:281px;height:556px;background:linear-gradient(180deg,var(--aqua-light),#c5eef6 50%,var(--aqua-light))}
.demo-title{position:absolute;top:6px;width:100%;text-align:center;font:800 12px "Open Sans",Arial,sans-serif;color:#6fb5c5}
.demo{position:absolute;left:6px;top:22px;width:269px;font-size:6.6px;font-weight:700}
.row{display:grid;grid-template-columns:98px 1fr 1fr 1fr;align-items:center;min-height:8.6px}
.row span:not(:first-child){text-align:center}
.row.head{background:#f4c9a0;height:13px;color:var(--white);margin-bottom:4px}
.row.head span:first-child{color:var(--blue);padding-left:4px}
.row.head span:not(:first-child){background:var(--orange);margin:0 3px;border-radius:2px;line-height:13px}
.label{color:var(--orange);font-size:6.4px;margin:3px 0 2px 2px;background:#bfe6ee;padding:1px 2px}
.group{background:rgba(255,255,255,.55);padding:2px 2px;margin-bottom:3px}
.row.pct span:not(:first-child){display:flex;justify-content:space-between;padding:0 3px;font-size:5.6px}
.row.pct i{font-style:normal}
.row.inc{background:var(--blue-light);color:#fff;height:11px}
.row.inc span:first-child{padding-left:3px}
.row.money{font-size:7.4px;min-height:12px}
.row.money span:not(:first-child){background:#fde6cf;margin:1px 3px;border-radius:2px}
.credit{position:absolute;left:8px;bottom:8px;display:flex;align-items:center;gap:6px;font-size:6px;color:#69b2c2}
.credit i{width:16px;height:12px;background:var(--orange)}

/* outside right */
.out-right{left:566px;top:36px;width:293px;height:556px;background:linear-gradient(180deg,#e6f7fb,var(--sky) 70%,#a9e3f0)}
.seize{position:absolute;top:20px;width:100%;text-align:center;font-family:Anton,Impact,sans-serif;color:var(--red);line-height:1}
.seize .s1{font-size:17px;color:var(--red);letter-spacing:1px}
.seize .s2{font-size:27px;color:var(--orange);letter-spacing:1px;-webkit-text-stroke:1px var(--red)}
.photo-b{left:0;top:120px;width:293px;height:170px;background:linear-gradient(180deg,#dfeef6 0%,#c7dbe9 45%,#a68c6a 70%,#8a8a80 100%)}
.plaza-name{position:absolute;top:225px;width:100%;text-align:center}
.plaza-name .n{font:22px/1 Anton,Impact,sans-serif;color:#e7f07a;letter-spacing:.5px}
.plaza-name .s{font:600 17px/1 "Dancing Script",cursive;color:#fff;margin-left:70px}
.badge{position:absolute;left:26px;top:270px;width:102px;height:82px;border-radius:50%;background:var(--red);border:3px solid #fff;display:flex;align-items:center;justify-content:center;text-align:center;font:800 8px/1.15 "Open Sans",Arial,sans-serif;color:#fff;padding:6px}
.photo-c{left:0;top:350px;width:293px;height:104px;background:linear-gradient(180deg,#cfe4ee 0%,#b9d0df 40%,#9e8d74 72%,#7e8a6c 100%)}
.photo-c-text{position:absolute;left:12px;top:366px;width:230px;font:italic 700 6.5px/1.3 "Open Sans",Arial,sans-serif;color:#ffe25a}
.address{position:absolute;left:96px;top:462px;width:188px;height:66px;background:var(--green-light);padding:8px 10px;color:#fff;font:700 8px/1.35 "Open Sans",Arial,sans-serif}
.address b{display:block;font-size:10px}

/* inside left */
.in-left{left:0;top:640px;width:281px;height:556px;background:linear-gradient(180deg,var(--olive-light),var(--olive) 55%,var(--olive-light))}
.overview-pill{position:absolute;left:12px;top:20px;width:80px;height:24px;border-radius:12px;background:#fff;color:var(--green);font:800 12px/24px "Open Sans",Arial,sans-serif;text-align:center;border:2px solid var(--olive-light)}
.photo-d{left:130px;top:12px;width:140px;height:46px;background:linear-gradient(180deg,#dfe6ea,#a99c86 70%,#8d8f82)}
.facts{position:absolute;left:44px;top:60px;width:170px;height:118px;border-radius:50%;background:var(--cream);border:5px solid #f7f0b6;display:flex;flex-direction:column;justify-content:center;align-items:center;font:400 7.5px/1.35 "Open Sans",Arial,sans-serif;color:#3a3a2a}
.facts b{font-weight:700}
.block{position:absolute;left:16px;width:260px;color:#fff;font:700 7px/1.35 "Open Sans",Arial,sans-serif;padding:5px 6px 5px 34px}
.block .tab{position:absolute;left:0;top:0;bottom:0;width:14px;display:flex;align-items:center;justify-content:center;writing-mode:vertical-rl;transform:rotate(180deg);font-size:5px;letter-spacing:.5px}
.block .cap{float:left;font:800 30px/0.9 "Open Sans",Arial,sans-serif;margin:1px 4px 0 0;color:#fff}
.b1{top:180px;background:#4f97b6;color:#fff}.b1 .tab{background:#3a7f9e}
.b2{top:252px;background:#bfe5f2;color:#3a7fa0}.b2 .cap{color:#3a7fa0}
.b3{top:310px;background:var(--green);color:#fff}
.b4{top:384px;background:#f2a552;color:#fff}.b4 .tab{background:#e38a36}
.b5{top:450px;background:#d5d3bc;color:#5b5b50}.b5 .cap{color:#5b5b50}.b5 .tab{background:#b7b49b;color:#fff}

/* inside central + right */
.in-spread{left:283px;top:640px;width:576px;height:556px;background:linear-gradient(180deg,#fdfbf0,#e8f3f4 30%,#dfeceb 100%)}
.spend-title{position:absolute;left:10px;top:14px;width:200px;height:20px;background:#fff;font:800 11px/20px "Open Sans",Arial,sans-serif;color:var(--orange);padding-left:4px;border-bottom:2px solid #f7d3a8}
.radius{position:absolute;left:236px;top:44px;font:800 8px "Open Sans",Arial,sans-serif;color:var(--orange)}
.pin{position:absolute;top:20px;width:40px;height:40px;border-radius:50% 50% 50% 0;transform:rotate(-45deg);background:radial-gradient(circle at 50% 50%,var(--orange),#f06a2a);}
.pin-text{position:absolute;top:32px;width:40px;text-align:center;font:800 7px "Open Sans",Arial,sans-serif;color:#fff}
.report-band{position:absolute;left:10px;top:62px;width:270px;height:15px;background:linear-gradient(90deg,var(--blue),var(--blue-light));color:#fff;font:700 8px/15px "Open Sans",Arial,sans-serif;padding-left:14px}
.spend{position:absolute;left:10px;top:80px;width:556px;font-size:7px}
.srow{display:grid;grid-template-columns:88px 182px 100px 100px 86px;align-items:center;height:9px;font-weight:700}
.srow span:nth-child(n+3){text-align:right;padding-right:22px}
.srow.total{height:14px;background:linear-gradient(90deg,#f6b06f,var(--red) 60%,#f58c7c);color:#fff;font-size:7px}
.srow.total span:first-child{grid-column:1/3;padding-left:6px}
.srow.cat{height:13px;margin-top:7px;background:linear-gradient(90deg,rgba(124,194,66,0),var(--green) 40%,var(--green-light));color:#fff;font-weight:700}
</style>
</head>
<body>
<div class="canvas">

  <div class="panel-labels" style="top:2px">
    <div class="lbl">Panel - 1<br>Outside Left</div>
    <div class="lbl">Panel - 2<br>Outside Central</div>
    <div class="lbl">Panel - 3<br>Outside Right (Front)</div>
  </div>

  <section class="panel out-left">
    <div class="sec-title">AERIAL MAP</div>
    <div class="ph map" role="img" aria-label="Street map of the area around the shopping center with its location pin"></div>
    <div class="ph photo-a" role="img" aria-label="Photo of the shopping center storefronts and pole sign"></div>
    <div class="traffic-title">TRAFFIC COUNT INFORMATION</div>
    <div class="traffic-heads"><span>STREET</span><span>CROSS STREET</span><span>MILES FROM</span><span>AVG DAILY VOLUME</span></div>
    <table class="traffic">
      <tr><td>W Harlan Crest Rd.</td><td>Larkin Ln</td><td>0.02 E</td><td>12,875</td></tr>
      <tr><td>N Ashby</td><td>Dr Pellam Ct.</td><td>0.04 S</td><td>6,654</td></tr>
      <tr><td>W Harlan Crest Rd.</td><td>Saddle Trl</td><td>0.03 NE</td><td>15,817</td></tr>
      <tr><td>State Hwy 88</td><td>Airfield Fwy</td><td>0.33 SW</td><td>142,402</td></tr>
      <tr><td>Airfield Fwy</td><td>N Ashby Dr.</td><td>0.02 NE</td><td>149,561</td></tr>
      <tr><td>W Harlan Crest Rd.</td><td>Fernway Dr.</td><td>0.04 W</td><td>14,152</td></tr>
      <tr><td>Coburn Rd.</td><td>Harlan Ct W.</td><td>0.03 S</td><td>15,333</td></tr>
      <tr><td>W Harlan Crest Rd.</td><td>Duchess Ln.</td><td>0.02 E</td><td>15,302</td></tr>
      <tr><td>Airfield Fwy</td><td>Brae Hill Dr.</td><td>0.05 SW</td><td>15,674</td></tr>
      <tr><td>State Hwy 88</td><td>District Line Rd.</td><td>0.21 E</td><td>15,275</td></tr>
    </table>
    <div class="tagline">The ideal space to operate your retail business</div>
  </section>

  <section class="panel out-central">
    <div class="demo-title">Demographic Summary Report</div>
    <div class="demo">
      <div class="row head"><span>RADIUS</span><span>1 Mile</span><span>3 Mile</span><span>5 Mile</span></div>
      <div class="label">POPULATION</div>
      <div class="group">
        <div class="row"><span>2019 Projection</span><span>13,954</span><span>112,287</span><span>272,105</span></div>
        <div class="row"><span>2014 Estimate</span><span>12,906</span><span>104,045</span><span>251,515</span></div>
        <div class="row"><span>2010 Census</span><span>12,215</span><span>99,109</span><span>237,504</span></div>
      </div>
      <div class="group">
        <div class="row"><span>Growth 2014 - 2019</span><span>8.12%</span><span>7.92%</span><span>8.19%</span></div>
        <div class="row"><span>Growth 2010 - 2014</span><span>5.66%</span><span>4.98%</span><span>5.90%</span></div>
      </div>
      <div class="group">
        <div class="row"><span>2014 Population by<br>Hispanic Origin</span><span>3,308</span><span>19,764</span><span>47,487</span></div>
      </div>
      <div class="group">
        <div class="row"><span>2014 Population By Race</span><span>12,906</span><span>104,045</span><span>251,515</span></div>
        <div class="row pct"><span>White</span><span><i>11,149</i><i>86.39%</i></span><span><i>90,430</i><i>86.91%</i></span><span><i>211,654</i><i>84.15%</i></span></div>
        <div class="row pct"><span>Black</span><span><i>896</i><i>6.94%</i></span><span><i>6,394</i><i>6.15%</i></span><span><i>20,024</i><i>7.96%</i></span></div>
        <div class="row pct"><span>Am. Indian &amp; Alaskan</span><span><i>152</i><i>1.18%</i></span><span><i>923</i><i>0.89%</i></span><span><i>2,246</i><i>0.89%</i></span></div>
        <div class="row pct"><span>Asian</span><span><i>353</i><i>2.74%</i></span><span><i>3,554</i><i>3.42%</i></span><span><i>11,287</i><i>4.49%</i></span></div>
        <div class="row pct"><span>Hawaiian &amp; Pacific Island</span><span><i>36</i><i>0.28%</i></span><span><i>401</i><i>0.39%</i></span><span><i>903</i><i>0.36%</i></span></div>
        <div class="row pct"><span>Other</span><span><i>320</i><i>2.48%</i></span><span><i>2,343</i><i>2.25%</i></span><span><i>5,400</i><i>2.15%</i></span></div>
      </div>
      <div class="label">HOUSEHOLDS</div>
      <div class="group">
        <div class="row"><span>2019 Projection</span><span>5,674</span><span>44,655</span><span>106,440</span></div>
        <div class="row"><span>2014 Estimate</span><span>5,252</span><span>41,409</span><span>98,391</span></div>
        <div class="row"><span>2010 Census</span><span>4,994</span><span>39,609</span><span>93,073</span></div>
        <div class="row"><span>Growth 2014 - 2019</span><span>8.04%</span><span>7.84%</span><span>8.18%</span></div>
        <div class="row"><span>Growth 2010 - 2014</span><span>0.97%</span><span>1.26%</span><span>2.59%</span></div>
        <div class="row pct"><span>Owner Occupied</span><span><i>2,214</i><i>42.16%</i></span><span><i>25,722</i><i>62.12%</i></span><span><i>62,127</i><i>63.14%</i></span></div>
        <div class="row pct"><span>Renter Occupied</span><span><i>3,038</i><i>57.84%</i></span><span><i>15,686</i><i>37.88%</i></span><span><i>36,264</i><i>36.86%</i></span></div>
      </div>
      <div class="group">
        <div class="row"><span>2014 Households by<br>HH Income</span><span>5,251</span><span>41,410</span><span>98,390</span></div>
      </div>
      <div class="row inc"><span>Income Range</span><span>1 Mile</span><span>3 Mile</span><span>5 Mile</span></div>
      <div class="group">
        <div class="row pct"><span>&lt;$25,000</span><span><i>1,581</i><i>30.11%</i></span><span><i>7,783</i><i>18.79%</i></span><span><i>17,503</i><i>17.79%</i></span></div>
        <div class="row pct"><span>$25,000 - $50,000</span><span><i>1,747</i><i>33.27%</i></span><span><i>10,806</i><i>26.10%</i></span><span><i>24,521</i><i>24.92%</i></span></div>
        <div class="row pct"><span>$50,000 - $75,000</span><span><i>792</i><i>15.08%</i></span><span><i>7,636</i><i>18.44%</i></span><span><i>18,613</i><i>18.92%</i></span></div>
        <div class="row pct"><span>$75,000 - $100,000</span><span><i>628</i><i>11.96%</i></span><span><i>6,273</i><i>15.15%</i></span><span><i>14,302</i><i>14.54%</i></span></div>
        <div class="row pct"><span>$100,000 - $125,000</span><span><i>221</i><i>4.21%</i></span><span><i>3,610</i><i>8.72%</i></span><span><i>8,610</i><i>8.75%</i></span></div>
        <div class="row pct"><span>$125,000 - $150,000</span><span><i>180</i><i>3.43%</i></span><span><i>2,265</i><i>5.47%</i></span><span><i>5,585</i><i>5.68%</i></span></div>
        <div class="row pct"><span>$150,000 - $200,000</span><span><i>37</i><i>0.70%</i></span><span><i>1,869</i><i>4.51%</i></span><span><i>5,348</i><i>5.44%</i></span></div>
        <div class="row pct"><span>$200,000+</span><span><i>65</i><i>1.24%</i></span><span><i>1,168</i><i>2.82%</i></span><span><i>3,908</i><i>3.97%</i></span></div>
      </div>
      <div class="group">
        <div class="row money"><span>2014 Avg<br>Household Income</span><span>$51,729</span><span>$71,417</span><span>$75,998</span></div>
        <div class="row money"><span>2014 Med<br>Household Income</span><span>$38,845</span><span>$56,960</span><span>$58,938</span></div>
      </div>
    </div>
    <div class="credit"><i></i>This copyrighted report is courtesy of Meridian Data Group Inc.</div>
  </section>

  <section class="panel out-right">
    <svg width="293" height="556" style="position:absolute;left:0;top:0" aria-hidden="true">
      <path d="M0 100 C90 70 200 130 293 95 L293 120 C200 150 90 95 0 125 Z" fill="#fff" opacity=".7"/>
      <path d="M0 470 C100 440 190 520 293 480 L293 556 L0 556 Z" fill="#fff" opacity=".45"/>
    </svg>
    <div class="seize"><div class="s1">SEIZE A PRIME</div><div class="s2">OPPORTUNITY</div></div>
    <div class="ph photo-b" role="img" aria-label="Photo of the shopping center building with its tall tenant pole sign"></div>
    <div class="plaza-name"><div class="n">WILLOWMERE COMMONS</div><div class="s">Shopping Center</div></div>
    <div class="badge">THE IDEAL SPACE TO OPERATE YOUR RETAIL BUSINESS</div>
    <div class="ph photo-c" role="img" aria-label="Photo of the shopping center frontage and parking lot"></div>
    <div class="photo-c-text">Experience high-visibility retail frontage beside a busy regional mall corridor</div>
    <div class="address"><b>Willowmere Commons</b>4410-4486 W Harlan Crest Rd,<br>Fairdale, TX 76099</div>
  </section>

  <div class="panel-labels" style="top:604px">
    <div class="lbl">Panel - 1<br>Inside Left</div>
    <div class="lbl">Panel - 2<br>Inside Central</div>
    <div class="lbl">Panel - 3<br>Inside Right</div>
  </div>

  <section class="panel in-left">
    <div class="overview-pill">OVERVIEW</div>
    <div class="ph photo-d" role="img" aria-label="Photo of the shopping center with its pole sign"></div>
    <div class="facts">
      <div><b>Building Type:</b> Gen. Retail</div>
      <div><b>Year Built:</b> 1979</div>
      <div><b>GLA:</b> 45,000 SF</div>
      <div><b>% Leased:</b> 39.36%</div>
      <div><b>Total Available:</b> 30,286 SF</div>
      <div><b>Rent/SF/Yr:</b> $15.28</div>
    </div>
    <div class="block b1"><span class="tab">STRATEGIC LOCALE</span><span class="cap">W</span>illowmere Commons is less than 600 feet from Willowmere Mall, a large enclosed upscale shopping mall in North Calder County with stores such as Lindqvist's, Harrow's and Mabry's.</div>
    <div class="block b2"><span class="cap">T</span>he shopping center also has direct freeway visibility and access from highway 88 which has a traffic count of 150,000 cars per day.</div>
    <div class="block b3"><span class="cap">W</span>illowmere Commons has excellent access. Exit to the north via State Highway 88 or to the south onto Harlan-Crest Road, a major 4 lane boulevard that runs right beside Willowmere Mall.</div>
    <div class="block b4"><span class="tab">SIGNAGE</span><span class="cap">A</span> large pole sign on Harlan Crest road with each tenant entrepreneur's name. Harlan Crest road has a daily traffic count of approximately 13,000 cars per day.</div>
    <div class="block b5"><span class="tab">SPACE</span><span class="cap">W</span>illowmere Commons Shopping Center has over 41,000 square feet of retail space and sits with two other properties with the same ownership on approximately 6 acres providing customers with abundant parking.</div>
    <div class="tagline">The ideal space to operate your retail business</div>
  </section>

  <section class="panel in-spread">
    <div class="ph" style="left:300px;top:80px;width:276px;height:476px;background:linear-gradient(180deg,rgba(190,214,224,.5),rgba(170,160,140,.35));" role="img" aria-label="Faded photo of the shopping center storefronts"></div>
    <div class="spend-title">CONSUMER SPENDING INFO.</div>
    <div class="radius">RADIUS</div>
    <div class="pin" style="left:300px"></div><div class="pin-text" style="left:300px">1 MILE</div>
    <div class="pin" style="left:400px"></div><div class="pin-text" style="left:400px">3 MILE</div>
    <div class="pin" style="left:500px"></div><div class="pin-text" style="left:500px">5 MILE</div>
    <div class="report-band">2014 CONSUMER SPENDING REPORT</div>
    <div class="spend">
      <div class="srow total"><span>TOTAL SPECIFIED CONSUMER SPENDING ($000s)</span><span>$117,341</span><span>$1,121,691</span><span>$2,752,922</span></div>

      <div class="srow cat"><span></span><span>Total Apparel</span><span>$6,961</span><span>$62,487</span><span>$154,011</span></div>
      <div class="srow"><span></span><span>Women's Apparel</span><span>2,650</span><span>25,146</span><span>62,028</span></div>
      <div class="srow"><span></span><span>Men's Apparel</span><span>1,447</span><span>13,365</span><span>32,863</span></div>
      <div class="srow"><span></span><span>Girl's Apparel</span><span>570</span><span>4,704</span><span>11,726</span></div>
      <div class="srow"><span></span><span>Boy's Apparel</span><span>382</span><span>3,264</span><span>8,121</span></div>
      <div class="srow"><span></span><span>Infant Apparel</span><span>360</span><span>2,806</span><span>6,873</span></div>
      <div class="srow"><span></span><span>Footwear</span><span>1,553</span><span>13,201</span><span>32,401</span></div>

      <div class="srow cat"><span></span><span>Total Entertainment &amp; Hobbies</span><span>$8,888</span><span>$85,254</span><span>$205,995</span></div>
      <div class="srow"><span></span><span>Entertainment</span><span>1,292</span><span>13,081</span><span>31,680</span></div>
      <div class="srow"><span></span><span>Audio &amp; Visual Equipment/Service</span><span>4,663</span><span>42,311</span><span>102,294</span></div>
      <div class="srow"><span></span><span>Reading Materials</span><span>330</span><span>3,632</span><span>8,710</span></div>
      <div class="srow"><span></span><span>Pets, Toys, &amp; Hobbies</span><span>2,603</span><span>26,231</span><span>63,312</span></div>

      <div class="srow cat"><span></span><span>Total Food and Alcohol</span><span>$31,785</span><span>$287,455</span><span>$698,276</span></div>
      <div class="srow"><span></span><span>Food At Home</span><span>17,843</span><span>155,681</span><span>375,975</span></div>
      <div class="srow"><span></span><span>Food Away From Home</span><span>11,870</span><span>112,929</span><span>276,559</span></div>
      <div class="srow"><span></span><span>Alcoholic Beverages</span><span>2,072</span><span>18,845</span><span>45,744</span></div>

      <div class="srow cat"><span></span><span>Total Household</span><span>$13,968</span><span>$147,929</span><span>$368,956</span></div>
      <div class="srow"><span></span><span>House Maintenance &amp; Repair</span><span>2,299</span><span>27,316</span><span>67,086</span></div>
      <div class="srow"><span></span><span>Household Equip &amp; Furnishings</span><span>6,000</span><span>60,810</span><span>150,608</span></div>
      <div class="srow"><span></span><span>Household Operations</span><span>4,414</span><span>44,974</span><span>112,519</span></div>
      <div class="srow"><span></span><span>Housing Costs</span><span>1,255</span><span>14,829</span><span>38,742</span></div>

      <div class="srow cat"><span></span><span>Total Transportation/Maint.</span><span>$34,908</span><span>$315,281</span><span>$816,246</span></div>
      <div class="srow"><span></span><span>Vehicle Purchases</span><span>10,753</span><span>110,195</span><span>274,574</span></div>
      <div class="srow"><span></span><span>Gasoline</span><span>18,628</span><span>165,152</span><span>401,345</span></div>
      <div class="srow"><span></span><span>Vehicle Expenses</span><span>442</span><span>6,339</span><span>16,651</span></div>
      <div class="srow"><span></span><span>Transportation</span><span>1,492</span><span>16,467</span><span>43,057</span></div>
      <div class="srow"><span></span><span>Automotive Repair &amp; Maintenance</span><span>3,595</span><span>33,032</span><span>80,639</span></div>

      <div class="srow cat"><span></span><span>Total Health Care</span><span>$6,153</span><span>$59,897</span><span>$142,884</span></div>
      <div class="srow"><span></span><span>Medical Services</span><span>3,229</span><span>31,698</span><span>76,495</span></div>
      <div class="srow"><span></span><span>Prescription Drugs</span><span>2,347</span><span>22,552</span><span>52,886</span></div>
      <div class="srow"><span></span><span>Medical Supplies</span><span>578</span><span>5,647</span><span>13,503</span></div>

      <div class="srow cat"><span></span><span>Total Education/Day Care</span><span>$6,223</span><span>$64,938</span><span>$165,187</span></div>
      <div class="srow"><span></span><span>Education</span><span>4,251</span><span>42,992</span><span>109,132</span></div>
      <div class="srow"><span></span><span>Fees &amp; Admissions</span><span>1,972</span><span>21,946</span><span>56,055</span></div>
    </div>
  </section>

</div>
</body>
</html>
```